Rw construct holdings pty ltd

This is a development and construction company. Website can be set up on our domain rwbuildgroup.net if we could change the domain to rwbuildgroup.com.au would be great

Want the page to have eye catching designs, red, black and white are the preffered colours.

Check out www.tolumine.com.au it is my former company with my partner which i am now venturing out on my own, that is the perfect example of the website i want even allot of the information would be the same

Industry/Entity Type

Construction

Coding

Coded - Design and coding required

Number of Pages Required

5+ page

Requirements
Must have
• Company logo eye catching designs

```html
<!DOCTYPE html>
<html lang="en">
<head>
<meta charset="utf-8">
<title>RW Build Group</title>
<link href="https://fonts.googleapis.com/css2?family=Ubuntu:wght@400;500;700&family=Open+Sans:ital,wght@0,400;0,600;0,700;1,400&display=swap" rel="stylesheet">
<style>
:root{
  --red:#e8141b;
  --red-dark:#c70f15;
  --black:#0d0d0d;
  --charcoal:#1c1c1e;
  --ink:#222;
  --muted:#666;
  --white:#fff;
  --line:#bdbdbd;
}
*{box-sizing:border-box;margin:0;padding:0}
html,body{width:1200px;height:4660px;overflow:hidden}
body{position:relative;background:var(--white);font-family:"Open Sans",sans-serif;color:var(--ink)}
.abs{position:absolute}
.heading{font-family:"Ubuntu",sans-serif;font-weight:500;font-size:60px;text-align:center;width:100%;color:var(--black)}
.heading .accent{color:var(--red)}
.btn{position:absolute;display:flex;align-items:center;justify-content:center;border-radius:30px;font-family:"Open Sans",sans-serif;font-weight:700;font-size:18px;color:var(--white);background:var(--black)}
.btn.red{background:var(--red)}

/* hero */
.hero{left:0;top:0;width:1200px;height:920px;background:linear-gradient(180deg,#3a3f46 0%,#565b62 45%,#2b2e33 100%)}
.hero-shade{left:0;top:0;width:1200px;height:920px;background:rgba(0,0,0,.35)}
.topbar{left:0;top:0;width:1200px;height:120px;background:rgba(10,10,10,.85)}
.brand{display:flex;align-items:center;gap:12px;font-family:"Ubuntu",sans-serif;font-weight:700;color:var(--white)}
.brand .mark{width:22px;height:22px;background:var(--red)}
.header-brand{left:180px;top:34px;font-size:34px}
.phone{left:860px;top:22px;font-size:18px;color:var(--red);font-weight:600;display:flex;gap:10px;align-items:center}
.nav{left:560px;top:66px;display:flex;gap:20px;font-size:19px;font-weight:600;color:var(--white)}
.nav .active{color:var(--red)}
.hero-title{left:0;top:300px;width:1200px;text-align:center;font-family:"Ubuntu",sans-serif;font-weight:500;font-size:54px;line-height:66px;color:var(--white)}

/* about */
.about-text{left:180px;top:960px;width:840px;font-size:17px;line-height:27px;text-align:center;color:var(--muted)}
.photo{position:absolute}

/* what we do */
.whatwedo{left:0;top:1568px;width:1200px;height:464px;background:var(--red)}
.feature{position:absolute;top:1760px;width:200px;text-align:center}
.feature svg{display:block;margin:0 auto 14px}
.feature h3{font-family:"Open Sans",sans-serif;font-size:17px;font-weight:700;color:var(--black);margin-bottom:6px}
.feature p{font-size:12px;line-height:16px;color:var(--black)}

/* services */
.service-card{position:absolute;top:2192px;width:256px;height:256px;box-shadow:0 4px 12px rgba(0,0,0,.25)}
.service-title{position:absolute;top:2500px;width:256px;text-align:center;font-family:"Ubuntu",sans-serif;font-weight:500;font-size:24px;color:var(--black)}
.service-text{position:absolute;top:2540px;width:256px;text-align:center;font-size:14px;line-height:19px;color:var(--ink)}

/* projects */
.projects{left:0;top:2748px;width:1200px;height:712px;background:linear-gradient(180deg,#2a2c30,#1a1b1e)}

/* partners */
.quote-card{position:absolute;top:3620px;width:400px;height:230px;border:2px solid var(--line);padding:34px 46px;text-align:center}
.quote-card p{font-style:italic;font-size:17px;line-height:23px;color:var(--ink)}
.quote-card .who{margin-top:14px;font-family:"Ubuntu",sans-serif;font-weight:500;font-size:22px;color:var(--red)}
.qmark{position:absolute;font-size:34px;font-weight:700;color:var(--ink)}

/* footer */
.footer-shape{left:0;top:3860px}
.footer-brand{left:600px;top:3970px;font-size:44px}
.footer-h{font-family:"Ubuntu",sans-serif;font-weight:500;color:var(--white)}
.field{position:absolute;background:var(--white);height:36px;font-size:12px;color:#777;padding:9px 10px}
.links{left:636px;top:4200px;font-size:18px;line-height:36px;color:var(--white)}
.contact{left:812px;top:4200px;font-size:16px;color:var(--white)}
.contact .row{display:flex;gap:14px;margin-bottom:22px;align-items:flex-start}
.social{position:absolute;top:4494px;width:34px;height:34px;border-radius:50%;background:var(--red)}
.copyright{left:0;top:4590px;width:1200px;height:70px;background:#050505;color:#888;font-size:14px;text-align:center;line-height:70px}
</style>
</head>
<body>

<!-- hero -->
<div class="abs hero" role="img" aria-label="Photo of a modern two-storey residential duplex at dusk"></div>
<div class="abs hero-shade"></div>
<svg class="abs" style="left:0;top:680px" width="1200" height="240" viewBox="0 0 1200 240" aria-hidden="true">
  <polygon points="0,40 640,240 0,240" fill="#fff"/>
  <polygon points="1200,190 1200,240 640,240" fill="#fff"/>
</svg>
<div class="abs topbar"></div>
<div class="abs brand header-brand"><span class="mark"></span>RW BUILD GROUP</div>
<div class="abs phone">
  <svg width="16" height="18" viewBox="0 0 16 18"><rect x="3" y="1" width="10" height="16" rx="2" fill="none" stroke="#e8141b" stroke-width="2"/><circle cx="8" cy="14" r="1.2" fill="#e8141b"/></svg>
  (123) 456 7890
</div>
<nav class="abs nav"><span class="active">Home</span><span>About</span><span>Services</span><span>Pages</span><span>Projects</span><span>Blog</span><span>Contact</span></nav>
<h1 class="abs hero-title">Innovative &amp; Quality Driven<br>Construction Services</h1>
<div class="btn red" style="left:505px;top:450px;width:190px;height:56px">GET TO KNOW</div>

<!-- about -->
<h2 class="abs heading" style="left:0;top:860px">About RW <span class="accent">Development</span></h2>
<p class="abs about-text">Sed ut perspiciatis unde omnis iste natus error sit voluptatem accusantium doloremque laudantium, totam rem aperiam, eaque ipsa quae ab illo inventore veritatis et quasi architecto beatae vitae dicta sunt explicabo. Nemo enim ipsam voluptatem quia voluptas sit aspernatur aut odit aut fugit, sed quia consequuntur magni dolores eos qui ratione voluptatem sequi nesciunt.</p>
<div class="photo" style="left:172px;top:1112px;width:856px;height:306px;background:linear-gradient(180deg,#cfd8e0 0%,#8d8a86 55%,#6e8a5a 100%)" role="img" aria-label="Rendering of a row of modern townhouses with timber screens"></div>
<div class="btn" style="left:508px;top:1462px;width:184px;height:56px">View More</div>

<!-- what we do -->
<div class="abs whatwedo"></div>
<h2 class="abs heading" style="left:0;top:1610px">What We Do</h2>
<div class="feature" style="left:142px">
  <svg width="80" height="80" viewBox="0 0 80 80"><polygon points="40,6 50,30 76,31 56,48 63,74 40,59 17,74 24,48 4,31 30,30" fill="#0d0d0d"/></svg>
  <h3>Exceptional Service</h3>
  <p>Lorem ipsum dolor sit amet, consectetur adipiscing elit, sed do eiusmod tempor incididunt ut.</p>
</div>
<div class="feature" style="left:380px">
  <svg width="80" height="80" viewBox="0 0 80 80"><path d="M40 6a24 24 0 0 0-14 43v9h28v-9A24 24 0 0 0 40 6z" fill="#0d0d0d"/><rect x="29" y="62" width="22" height="5" fill="#0d0d0d"/><rect x="32" y="70" width="16" height="5" fill="#0d0d0d"/></svg>
  <h3>Strategic</h3>
  <p>Lorem ipsum dolor sit amet, consectetur adipiscing elit, sed do eiusmod tempor incididunt ut.</p>
</div>
<div class="feature" style="left:620px">
  <svg width="80" height="80" viewBox="0 0 80 80"><circle cx="33" cy="33" r="23" fill="none" stroke="#0d0d0d" stroke-width="8"/><rect x="50" y="54" width="26" height="11" rx="3" transform="rotate(45 50 54)" fill="#0d0d0d"/><circle cx="33" cy="33" r="8" fill="#0d0d0d"/></svg>
  <h3>Transparency</h3>
  <p>Lorem ipsum dolor sit amet, consectetur adipiscing elit, sed do eiusmod tempor incididunt ut.</p>
</div>
<div class="feature" style="left:858px">
  <svg width="80" height="80" viewBox="0 0 80 80"><rect x="14" y="10" width="52" height="66" rx="5" fill="none" stroke="#0d0d0d" stroke-width="6"/><rect x="28" y="4" width="24" height="12" rx="3" fill="#0d0d0d"/><path d="M24 32l4 4 7-7M24 48l4 4 7-7" fill="none" stroke="#0d0d0d" stroke-width="4"/><rect x="40" y="31" width="16" height="4" fill="#0d0d0d"/><rect x="40" y="47" width="16" height="4" fill="#0d0d0d"/><rect x="24" y="61" width="32" height="4" fill="#0d0d0d"/></svg>
  <h3>Accountability</h3>
  <p>Lorem ipsum dolor sit amet, consectetur adipiscing elit, sed do eiusmod tempor incididunt ut.</p>
</div>

<!-- services -->
<h2 class="abs heading" style="left:0;top:2080px">Our <span class="accent">Services</span></h2>
<div class="service-card" style="left:172px;background:linear-gradient(180deg,#b9cfe6,#9a8f82 60%,#7b7064)" role="img" aria-label="Construction site with concrete slab and steel reinforcement"></div>
<div class="service-card" style="left:460px;background:linear-gradient(180deg,#d9dde2,#5a5652 55%,#3b3a38)" role="img" aria-label="Completed modern house build"></div>
<div class="service-card" style="left:748px;background:linear-gradient(180deg,#5b8fd6,#cfd3d6 55%,#8e8b88)" role="img" aria-label="Renovated two-storey residence"></div>
<div class="service-title" style="left:172px">CONSTRUCTION</div>
<div class="service-title" style="left:460px">HOUSE BUILDS</div>
<div class="service-title" style="left:748px">RENOVATIONS</div>
<p class="service-text" style="left:172px">Lorem ipsum dolor sit amet, consectetur adipiscing elit, sed do ullamcorper tempor vel facilisis.</p>
<p class="service-text" style="left:460px">Lorem ipsum dolor sit amet, consectetur adipiscing elit, sed do ullamcorper tempor vel facilisis.</p>
<p class="service-text" style="left:748px">Lorem ipsum dolor sit amet, consectetur adipiscing elit, sed do ullamcorper tempor vel facilisis.</p>
<div class="btn red" style="left:214px;top:2626px;width:172px;height:48px">READ MORE</div>
<div class="btn" style="left:502px;top:2626px;width:172px;height:48px">READ MORE</div>
<div class="btn" style="left:790px;top:2626px;width:172px;height:48px">READ MORE</div>

<!-- projects -->
<div class="abs projects"></div>
<h2 class="abs heading" style="left:0;top:2800px;color:var(--white)">Latest Projects</h2>
<div class="photo" style="left:172px;top:2900px;width:416px;height:200px;background:linear-gradient(135deg,#8c8a86,#4d4b48)" role="img" aria-label="Modern home facade with garage"></div>
<div class="photo" style="left:608px;top:2900px;width:192px;height:200px;background:linear-gradient(180deg,#d6dde4,#55524f)" role="img" aria-label="Two-storey townhouse"></div>
<div class="photo" style="left:820px;top:2900px;width:208px;height:200px;background:linear-gradient(180deg,#6a99d8,#bfc1c2 60%,#7c7a76)" role="img" aria-label="Contemporary duplex under blue sky"></div>
<div class="photo" style="left:172px;top:3112px;width:196px;height:188px;background:linear-gradient(180deg,#b7cbe0,#8f8272)" role="img" aria-label="Slab preparation on building site"></div>
<div class="photo" style="left:388px;top:3112px;width:204px;height:188px;background:linear-gradient(180deg,#cfd5db,#4f4c49)" role="img" aria-label="Row of new townhouses"></div>
<div class="photo" style="left:612px;top:3112px;width:416px;height:188px;background:linear-gradient(180deg,#c8cdd2,#9a9894)" role="img" aria-label="Freshly poured concrete slab"></div>
<div class="btn red" style="left:505px;top:3356px;width:190px;height:52px">View More</div>

<!-- partners -->
<h2 class="abs heading" style="left:0;top:3510px">From Our <span class="accent">Partners</span></h2>
<div class="quote-card" style="left:172px">
  <span class="qmark" style="left:18px;top:8px">“</span><span class="qmark" style="right:18px;bottom:52px">”</span>
  <p>Lorem ipsum dolor sit amet, cons adipiscing elit, sed do eiusmod tempor ullamco commodo viverra maecenas accumsan lacus vel facilisis.</p>
  <div class="who">Marcus Hale</div>
</div>
<div class="quote-card" style="left:620px">
  <span class="qmark" style="left:18px;top:8px">“</span><span class="qmark" style="right:18px;bottom:52px">”</span>
  <p>Lorem ipsum dolor sit amet, cons adipiscing elit, sed do eiusmod tempor ullamco commodo viverra maecenas accumsan lacus vel facilisis.</p>
  <div class="who">Dana Pirelli</div>
</div>

<!-- footer -->
<svg class="abs footer-shape" width="1200" height="800" viewBox="0 0 1200 800" aria-hidden="true">
  <polygon points="0,140 680,0 1200,0 1200,800 0,800" fill="#0d0d0d"/>
</svg>
<div class="abs brand footer-brand"><span class="mark"></span>RW BUILD GROUP</div>
<h3 class="abs footer-h" style="left:172px;top:4092px;font-size:38px">Get In Touch</h3>
<div class="field" style="left:172px;top:4172px;width:192px">First Name</div>
<div class="field" style="left:380px;top:4172px;width:192px">Last Name</div>
<div class="field" style="left:172px;top:4224px;width:192px">Email</div>
<div class="field" style="left:380px;top:4224px;width:192px">Phone Number</div>
<div class="field" style="left:172px;top:4276px;width:400px;height:70px">Message</div>
<div class="btn red" style="left:172px;top:4432px;width:128px;height:48px;border-radius:0">SUBMIT</div>

<h3 class="abs footer-h" style="left:636px;top:4150px;font-size:24px">Explore</h3>
<div class="abs links">Home<br>About<br>Services<br>Projects<br>Blog</div>

<h3 class="abs footer-h" style="left:812px;top:4150px;font-size:24px">Contact</h3>
<div class="abs contact">
  <div class="row"><svg width="16" height="22" viewBox="0 0 16 22"><path d="M8 1a7 7 0 0 0-7 7c0 6 7 13 7 13s7-7 7-13a7 7 0 0 0-7-7z" fill="#e8141b"/><circle cx="8" cy="8" r="2.5" fill="#0d0d0d"/></svg><span>123,1 Loreum ipsum<br>dolor sit ametur<br>lorem ipsum 444</span></div>
  <div class="row"><svg width="16" height="18" viewBox="0 0 16 18"><path d="M3 1l4 4-2 3 5 5 3-2 4 4-3 3C8 18 0 10 1 4z" fill="#e8141b"/></svg><span>+1 666 5555 444</span></div>
  <div class="row"><svg width="18" height="14" viewBox="0 0 18 14"><rect x="1" y="1" width="16" height="12" fill="#e8141b"/><path d="M1 1l8 7 8-7" fill="none" stroke="#0d0d0d" stroke-width="1.5"/></svg><span>info@companyname.com</span></div>
</div>

<h3 class="abs footer-h" style="left:636px;top:4490px;font-size:30px">Stay Connected:</h3>
<div class="social" style="left:904px"></div>
<div class="social" style="left:952px"></div>
<div class="social" style="left:1000px"></div>

<div class="abs copyright">COPYRIGHT 2021 ALL RIGHTS RESERVED · TERMS &amp; CONDITIONS</div>

</body>
</html>
```